Inbound Tour Operator Needs Product Brochure Design

We are an inbound Russian tour operator, and we need a four panel brochure (standard 8x11) for our featured tour package "Marvels of the Drylands" with two categories: standard pricing and upgraded pricing.

The 10 day itinerary routing (can be seen on our website http://bluecomettravel.example/en/tours/marvels-of-the-drylands-11-days/) would be the same for both categories, with the difference being in transporation type, hotels per itinerary, and pricing.

Target Market(s)

Russian Tourists

Requirements
Must have
• The front cover should have an image portraying the wild west, or anything else pertaining to "Marvels of the Drylands", it should also have the tour title, and a short description reading "California, Nevada, Arizona, Utah - 11 Days"

The ideal design should have the itinerary in the center of the inside fold (towards the bottom), left side would be dedicated to "Marvels of the Drylands - Group Bus Tour" with information about included hotels, services, dates of departure, and additional notes. Right side would be dedicated to "Marvels of the Drylands - VIP Package" with information about included hotels, services, dates of departure, and additional notes. Large photos depicting tourists, sightseeing, or southwest points of interest would be preferred (we have licensed pixvault photos if needed)

The back should be a more relaxed, open design, with space in the center top for client testimonials, and company contact information on the bottom center.

Document must be in editable format (Photoshop File) as we will need to translate the document into Russian.
Nice to have
• Incorporating the style and layout of our website, or at least the color scheme - www.bluecomettravel.example

```html
<!DOCTYPE html>
<html lang="en">
<head>
<meta charset="utf-8">
<title>Blue Comet Travel – Marvels of the Drylands Brochure</title>
<link rel="stylesheet" href="https://fonts.googleapis.com/css2?family=Arimo:wght@400;700&family=Montserrat:wght@400;500&family=Roboto+Condensed:wght@700&display=swap">
<style>
  :root {
    --gold: #f2c21b;
    --ink: #0c0c0c;
    --panel-grey: #eff0f1;
    --text-grey: #6a6a6a;
    --quote-grey: #444;
    --paper: #ffffff;
    --cream: #fdf6d8;
  }
  * { margin: 0; padding: 0; box-sizing: border-box; }
  html, body { width: 1200px; height: 786px; overflow: hidden; background: var(--paper); }
  .spread { position: relative; width: 1200px; height: 786px; font-family: "Montserrat", sans-serif; }

  /* ---------- back panel ---------- */
  .back { position: absolute; left: 0; top: 0; width: 600px; height: 786px; background: var(--paper); }
  .back__header { position: absolute; left: 0; top: 0; width: 600px; height: 203px; background: var(--ink); }
  .back__tab { position: absolute; left: 0; top: 152px; width: 272px; height: 52px; }
  .back__tab-title { position: absolute; left: 56px; top: 168px; font-family: "Roboto Condensed", sans-serif; font-weight: 700; font-size: 18px; color: #1a1a1a; letter-spacing: .2px; }
  .testimonials { position: absolute; left: 0; top: 203px; width: 600px; height: 363px; background: var(--panel-grey); }
  .testimonial { position: absolute; font-size: 7.5px; line-height: 10px; color: var(--text-grey); text-align: justify; }
  .testimonial .q-open, .testimonial .q-close { font-family: "Arimo", sans-serif; font-weight: 700; color: var(--quote-grey); font-size: 26px; line-height: 0; letter-spacing: -2px; }
  .testimonial .q-open { position: relative; top: 8px; margin-right: 2px; }
  .testimonial .q-close { position: relative; top: 11px; margin-left: 3px; }
  .testimonial__author { display: block; text-align: right; color: var(--gold); font-size: 6.5px; line-height: 8px; margin-top: 10px; }
  .t1 { left: 58px; top: 60px; width: 238px; }
  .t2 { left: 324px; top: 60px; width: 234px; }
  .t3 { left: 324px; top: 184px; width: 234px; }
  .t4 { left: 58px; top: 262px; width: 238px; }
  .t5 { left: 324px; top: 262px; width: 234px; }

  .brand { position: absolute; display: flex; align-items: center; gap: 8px; font-family: "Arimo", sans-serif; font-weight: 400; color: #151515; white-space: nowrap; }
  .brand__dot { border-radius: 50%; background: var(--gold); flex: none; }
  .brand--back { left: 44px; top: 628px; font-size: 22px; }
  .brand--back .brand__dot { width: 24px; height: 24px; }

  .contact { position: absolute; font-size: 8.4px; line-height: 16px; color: #222; font-style: normal; white-space: nowrap; }
  .contact__row { display: flex; align-items: center; gap: 7px; }
  .contact__row svg { flex: none; }
  .contact--address { left: 48px; top: 710px; }
  .contact--address .contact__line2 { padding-left: 17px; }
  .contact--web { left: 240px; top: 710px; }
  .back__photo { position: absolute; left: 407px; top: 632px; width: 170px; height: 113px; background: linear-gradient(160deg, #e8e4dc 0%, #cfc8ba 55%, #5f6248 100%); }
  .back__footer-bar { position: absolute; left: 0; top: 762px; width: 600px; height: 24px; background: var(--gold); }

  /* ---------- front cover ---------- */
  .cover { position: absolute; left: 600px; top: 0; width: 600px; height: 786px; background: var(--ink); }
  .cover__masthead { position: absolute; left: 0; top: 0; width: 600px; height: 198px; background: var(--paper); border-bottom: 3px solid var(--gold); }
  .brand--cover { right: 52px; top: 132px; font-size: 32px; }
  .brand--cover .brand__dot { width: 34px; height: 34px; }
  .gallery { position: absolute; left: 0; width: 600px; display: grid; grid-template-columns: 193px 193px 196px; column-gap: 9px; }
  .gallery--top { top: 214px; height: 129px; }
  .gallery--bottom { top: 424px; height: 128px; }
  .gallery__photo { height: 100%; }
  .photo-rock { background: linear-gradient(140deg, #7a3f24 0%, #a85a34 45%, #3f7a2a 100%); }
  .photo-strip { background: linear-gradient(180deg, #0b0b10 0%, #3a2a12 55%, #d19a3a 80%, #18140e 100%); }
  .photo-valley { background: linear-gradient(180deg, #6fa3d8 0%, #b4c6cf 35%, #2f5a2c 70%, #a38c52 100%); }
  .photo-desert { background: linear-gradient(170deg, #8db6e0 0%, #8a7a86 35%, #c9b48c 70%, #e2cfa8 100%); }
  .photo-palm { background: linear-gradient(170deg, #1f63c6 0%, #4a88d8 45%, #2d5a2a 75%, #8c9aa8 100%); }
  .photo-harbor { background: linear-gradient(180deg, #8fb6de 0%, #6f8aa0 45%, #4c7fa8 75%, #9fb7c8 100%); }
  .cover__title { position: absolute; left: 0; top: 372px; width: 600px; text-align: center; font-family: "Arimo", sans-serif; font-weight: 700; font-size: 24px; color: var(--gold); letter-spacing: .3px; }
  .cover__band { position: absolute; left: 7px; top: 566px; width: 573px; height: 49px; }
  .cover__subtitle { position: absolute; left: 0; top: 578px; width: 600px; text-align: center; font-family: "Arimo", sans-serif; font-weight: 700; font-size: 18px; color: var(--cream); text-shadow: 0 1px 1px rgba(0,0,0,.35); }
  .cover__subtitle strong { color: var(--ink); text-shadow: none; }
  .cover__web { position: absolute; left: 0; top: 736px; width: 600px; display: flex; justify-content: center; align-items: center; gap: 6px; font-size: 12px; color: #f2f2f2; letter-spacing: .6px; }
</style>
</head>
<body>
<main class="spread">

  <section class="back">
    <div class="back__header"></div>
    <svg class="back__tab" viewBox="0 0 272 52" aria-hidden="true"><polygon points="0,0 246,0 272,52 0,52" fill="var(--gold)"/></svg>
    <h2 class="back__tab-title">TESTIMONIALS</h2>

    <div class="testimonials">
      <p class="testimonial t1"><span class="q-open">“</span>Impression, feeling and understanding of the country largely depends on how you presented it, and how the information on it was presented. Pavel Orlov coped well with the mission and did everything possible to everyone in our group loved America. Optimally, a program, all the stories, the facts were accompanied by high-quality illustrations - themed movies, music, postcards, books. The tour guide was always thematically stylishly dressed, gallant, historically grounded and informative. I am grateful to the host of "Blue Comet" and personally Pavel Orlov for a rich, informative and very well prepared program! It is unlikely that in 11 days we could have someone to show and tell more. Thank you and I wish you strength, prosperity and good tourists! Success and prosperity to you!<span class="q-close">”</span><span class="testimonial__author">— Maria Ivanova</span></p>

      <p class="testimonial t2"><span class="q-open">“</span>A week ago, has returned to Moscow from a most interesting tour of the southwest United States. Canyons, Death Valley and Yosemite Park made a lasting impression. Thanks for the interesting program and the good organization of the tour. I want to express special thanks to our guide, Pavel Orlov, people Hobbies and a true professional.<span class="q-close">”</span><span class="testimonial__author">— Olga Smirnova, Moscow</span></p>

      <p class="testimonial t3"><span class="q-open">“</span>Dear Partners, thank you very much for the nice tour, great route, good organization, tourists dovolno. Reviews are good, the hotels are good.<span class="q-close">”</span><span class="testimonial__author">— Sergey Kuznetsov</span></p>

      <p class="testimonial t4"><span class="q-open">“</span>The findings alone - the tour is excellent! organization, service, surprises - all at the highest level. There is a brand thing, and there is brand experience. This is Las Vegas, Death Valley, and the Mohave Desert. In general, thank you so much!<span class="q-close">”</span><span class="testimonial__author">— Elena Popova</span></p>

      <p class="testimonial t5"><span class="q-open">“</span>Dear Partners, thank you very much for the nice tour, great route, good organization, tourists dovolno. Reviews are good, the hotels are good.<span class="testimonial__author">— Anna Volkova</span></p>
    </div>

    <div class="brand brand--back"><span class="brand__dot"></span>Blue Comet Travel</div>

    <address class="contact contact--address">
      <div class="contact__row">
        <svg width="10" height="12" viewBox="0 0 10 12" aria-hidden="true"><path d="M5 0a4 4 0 0 1 4 4c0 3-4 8-4 8S1 7 1 4a4 4 0 0 1 4-4z" fill="var(--gold)"/><circle cx="5" cy="4" r="1.5" fill="#fff"/></svg>
        <span>4150 Canyon Vista Ave. Suite #310</span>
      </div>
      <div class="contact__line2">Mesa Ridge, CA 90112</div>
    </address>

    <div class="contact contact--web">
      <div class="contact__row">
        <svg width="11" height="8" viewBox="0 0 11 8" aria-hidden="true"><rect width="11" height="8" fill="var(--gold)"/><path d="M0 0l5.5 4.5L11 0" stroke="#fff" fill="none"/></svg>
        <span>info@bluecomettravel.example</span>
      </div>
      <div class="contact__row">
        <svg width="11" height="11" viewBox="0 0 11 11" aria-hidden="true"><circle cx="5.5" cy="5.5" r="5.5" fill="var(--gold)"/></svg>
        <span>www.bluecomettravel.example</span>
      </div>
    </div>

    <div class="back__photo" role="img" aria-label="Photo of an alligator with open jaws on pale sand"></div>
    <div class="back__footer-bar"></div>
  </section>

  <section class="cover">
    <header class="cover__masthead">
      <div class="brand brand--cover"><span class="brand__dot"></span>Blue Comet Travel</div>
    </header>

    <div class="gallery gallery--top">
      <div class="gallery__photo photo-rock" role="img" aria-label="Photo of red sandstone canyon cliffs with green trees"></div>
      <div class="gallery__photo photo-strip" role="img" aria-label="Photo of the Las Vegas Strip lit up at night"></div>
      <div class="gallery__photo photo-valley" role="img" aria-label="Photo of a granite dome above a pine forest valley"></div>
    </div>

    <h1 class="cover__title">MARVELS OF THE DRYLANDS</h1>

    <div class="gallery gallery--bottom">
      <div class="gallery__photo photo-desert" role="img" aria-label="Photo of eroded desert badlands under a blue sky"></div>
      <div class="gallery__photo photo-palm" role="img" aria-label="Photo of a palm tree beside street signs against a blue sky"></div>
      <div class="gallery__photo photo-harbor" role="img" aria-label="Photo of a city skyline behind a marina with boats"></div>
    </div>

    <svg class="cover__band" viewBox="0 0 573 49" aria-hidden="true"><polygon points="0,0 573,0 549,49 24,49" fill="var(--gold)"/></svg>
    <p class="cover__subtitle">CALIFORNIA, NEVADA, ARIZONA, UTAH - <strong>11 DAYS</strong></p>

    <p class="cover__web">
      <svg width="10" height="10" viewBox="0 0 10 10" aria-hidden="true"><circle cx="5" cy="5" r="4.4" fill="none" stroke="#f2f2f2" stroke-width="1"/><ellipse cx="5" cy="5" rx="2" ry="4.4" fill="none" stroke="#f2f2f2" stroke-width=".8"/><path d="M.6 5h8.8" stroke="#f2f2f2" stroke-width=".8"/></svg>
      www.bluecomettravel.example
    </p>
  </section>

</main>
</body>
</html>
```